Business Cards for a company that provides webstore services to veterinarians

We need business cards designed for our main service PawCartHub. PawCartHub is a webstore that veterinarian clinics can use to that will allow their clients to purchase products for their pets. Our company is Brindlow Veterinary Solutions (Brindlow Veterinary Solutions). Our mission statement is We love pets! We will do everything possible to facilitate along, healthy and happy relationship with their families.

Target Market(s)

Veterinarians

Industry/Entity Type

Veterinary

Contact Information for Business Card

I would like the design to incorporate the colours our our company. Cards should have room for employee name, title (only necessary in two instances), phone number, mobile number, email address and linkedin symbol and related profile name ie Marla Quinton. I would like the PawCartHub logo to appear on one side and Brindlow Veterinary Solutions logo to appear on the other. I will need both an english and french version. I can provide the french translation. Please focus on english version and then we will translate

Colors

Designer to choose colors to be used in the design.

Requirements
Must have
• one side - PawCartHub logo with persons name, phone number, mobile number, email address
• second side - Brindlow Veterinary Solutions logo
• colours should be consistent with our company. colours are as follows:
• Red
• RGB: 190 / 30 / 45
• CYMK: 14 / 100 / 90 /10
• Hex: #BE1E2D
• Gray
• RGB: 88 / 89 / 86
• CYMK: 3 / 2 / 0 /64
• Hex: #585956
Nice to have
• address of company - can be on either side address is 4817 Feldmoor Street Suite 305 Burlington ON K2R 6T4. Toll free number will vary depending on person
• Linkedin symbol and name of person
• on second side with Brindlow Veterinary Solutions logo our company's mission statement
Should not have
• nothing comes to mind

```html
<!DOCTYPE html>
<html lang="en">
<head>
<meta charset="utf-8">
<title>PawCartHub Business Cards</title>
<link href="https://fonts.googleapis.com/css2?family=Open+Sans:wght@400;600;700&display=swap" rel="stylesheet">
<style>
  :root {
    --brand-red: #BE1E2D;
    --brand-gray: #6E6E6E;
    --page-bg: #9aa3ac;
    --ink-light: #ffffff;
    --card-radius: 34px;
  }
  * { box-sizing: border-box; margin: 0; padding: 0; }
  html, body { width: 1200px; height: 1200px; overflow: hidden; }
  body {
    background: var(--page-bg);
    font-family: "Open Sans", Arial, sans-serif;
    display: flex;
    flex-direction: column;
    align-items: center;
    justify-content: center;
    gap: 56px;
  }
  .card {
    position: relative;
    width: 900px;
    height: 514px;
    border-radius: var(--card-radius);
    overflow: hidden;
    background: var(--brand-gray);
    box-shadow: 0 10px 24px rgba(0,0,0,0.28);
  }

  /* Front */
  .card-front .brand-band {
    position: absolute; left: 0; top: 0; right: 0;
    height: 280px;
    background: var(--brand-red);
    display: flex; align-items: center; justify-content: center;
  }
  .wordmark {
    display: flex; align-items: center; gap: 22px;
    color: var(--ink-light);
    font-weight: 600;
    font-size: 96px;
    letter-spacing: -1px;
  }
  .wordmark-dot {
    width: 40px; height: 40px; border-radius: 50%;
    background: var(--ink-light);
  }
  .holder {
    position: absolute; left: 56px; top: 318px;
    color: var(--ink-light);
    font-size: 22px; line-height: 1.35;
  }
  .holder-name {
    color: var(--brand-red);
    font-weight: 700; font-size: 26px;
    text-transform: uppercase; letter-spacing: 0.5px;
  }
  .contacts {
    position: absolute; right: 56px; top: 318px;
    list-style: none;
    color: var(--ink-light);
    font-size: 24px; line-height: 1.45;
  }
  .contacts li { display: flex; align-items: center; gap: 14px; }
  .contacts svg { width: 20px; height: 20px; flex: none; }

  /* Back */
  .card-back .base-stripe {
    position: absolute; left: 0; right: 0; bottom: 0;
    height: 62px; background: var(--brand-red);
  }
  .back-mark {
    position: absolute; left: 0; right: 0; top: 150px;
    display: flex; flex-direction: column; align-items: center; gap: 22px;
  }
  .back-wordmark {
    display: flex; align-items: center; gap: 18px;
    color: var(--brand-red);
    font-weight: 700; font-size: 54px; line-height: 1.1;
  }
  .back-wordmark-dot {
    width: 34px; height: 34px; border-radius: 50%;
    background: var(--brand-red);
    flex: none;
  }
  .tagline {
    color: var(--ink-light);
    font-weight: 700; font-size: 22px; letter-spacing: 1px;
    text-transform: uppercase;
  }
</style>
</head>
<body>

  <section class="card card-front">
    <div class="brand-band">
      <div class="wordmark"><span>PawCartHub</span><span class="wordmark-dot"></span></div>
    </div>

    <div class="holder">
      <p class="holder-name">Marla Quinton</p>
      <p>Manager</p>
      <p>4817 Feldmoor Street Suite 305</p>
      <p>Halvern ON K2R 6T4</p>
    </div>

    <ul class="contacts">
      <li>
        <svg viewBox="0 0 20 20"><rect x="5" y="1" width="10" height="18" rx="2" fill="none" stroke="#BE1E2D" stroke-width="2"/><circle cx="10" cy="15.5" r="1.2" fill="#BE1E2D"/></svg>
        (555) 218 4470
      </li>
      <li>
        <svg viewBox="0 0 20 20"><path d="M4 2 L8 2 L9 6 L7 8 Q9 12 12 13 L14 11 L18 12 L18 16 Q18 18 16 18 Q3 17 2 4 Q2 2 4 2 Z" fill="#BE1E2D"/></svg>
        (555) 218 4471
      </li>
      <li>
        <svg viewBox="0 0 20 20"><rect x="1" y="4" width="18" height="12" rx="1.5" fill="none" stroke="#BE1E2D" stroke-width="2"/><path d="M2 5 L10 11 L18 5" fill="none" stroke="#BE1E2D" stroke-width="2"/></svg>
        hello@pawcarthub.com
      </li>
      <li>
        <svg viewBox="0 0 20 20"><circle cx="10" cy="10" r="8" fill="none" stroke="#BE1E2D" stroke-width="2"/><ellipse cx="10" cy="10" rx="3.5" ry="8" fill="none" stroke="#BE1E2D" stroke-width="1.6"/><line x1="2" y1="10" x2="18" y2="10" stroke="#BE1E2D" stroke-width="1.6"/></svg>
        www.pawcarthub.com
      </li>
    </ul>
  </section>

  <section class="card card-back">
    <div class="back-mark">
      <div class="back-wordmark"><span class="back-wordmark-dot"></span><span>Brindlow Veterinary Solutions</span></div>
      <p class="tagline">We Love Pets, Every Day</p>
    </div>
    <div class="base-stripe"></div>
  </section>

</body>
</html>
```